serious, thorough, light and simple - that's my advice and mediations

My business card should combine my logo (uploaded file) and my homepage (https://fellor-mediation.webnestsite.com).

Contact Information for Business Card

Name: Sabine Fellor di Vanti
Phone: 076 412 58 94
mail: sfellor@postkiv.ch
web: www.fellor-di-vanti.ch

```html
<!DOCTYPE html>
<html lang="de">
<head>
<meta charset="utf-8">
<title>Visitenkarte – Sabine Fellor di Vanti</title>
<link rel="stylesheet" href="https://fonts.googleapis.com/css2?family=Arimo:wght@400;700&display=swap">
<style>
  :root {
    --backdrop: #000000;
    --card: #2f3032;
    --card-edge: #36373a;
    --ink: #ffffff;
    --divider: #8a8b8d;
  }
  * { margin: 0; padding: 0; box-sizing: border-box; }
  html, body {
    width: 1200px; height: 900px; overflow: hidden;
    background: var(--backdrop);
    font-family: "Arimo", Arial, sans-serif;
    color: var(--ink);
  }
  .canvas { position: relative; width: 1200px; height: 900px; }

  .card {
    position: absolute;
    width: 458px; height: 280px;
    border-radius: 14px;
    background: linear-gradient(180deg, var(--card-edge) 0%, var(--card) 100%);
  }
  .card--front { left: 138px; top: 266px; }
  .card--back  { left: 625px; top: 268px; }

  .brand { position: absolute; display: flex; align-items: center; gap: 8px; }
  .brand__dot { border: 2px solid var(--ink); border-radius: 50%; flex: none; }
  .brand__name { font-weight: 400; color: var(--ink); white-space: nowrap; line-height: 1; }

  .card--front .brand { left: 30px; top: 128px; }
  .card--front .brand__dot { width: 18px; height: 18px; }
  .card--front .brand__name { font-size: 23px; }

  .card--back .brand { left: 50%; top: 120px; transform: translateX(-50%); gap: 10px; }
  .card--back .brand__dot { width: 26px; height: 26px; }
  .card--back .brand__name { font-size: 36px; }

  .divider {
    position: absolute; left: 232px; top: 89px;
    width: 1px; height: 108px;
    background: linear-gradient(180deg, transparent, var(--divider) 20%, var(--divider) 80%, transparent);
  }

  .contact { position: absolute; left: 256px; top: 93px; }
  .contact__name {
    font-weight: 700; font-size: 13px; letter-spacing: 0.2px;
    text-transform: uppercase; margin-bottom: 36px;
  }
  .contact__list { list-style: none; }
  .contact__item {
    display: flex; align-items: center; gap: 4px;
    font-size: 12.5px; line-height: 16.5px;
  }
  .contact__icon { width: 11px; height: 11px; flex: none; }
</style>
</head>
<body>
<main class="canvas">

  <section class="card card--front" aria-label="Vorderseite">
    <div class="brand">
      <span class="brand__dot"></span>
      <span class="brand__name">Wege im Dialog</span>
    </div>

    <div class="divider"></div>

    <div class="contact">
      <p class="contact__name">Sabine Fellor di Vanti</p>
      <ul class="contact__list">
        <li class="contact__item">
          <svg class="contact__icon" viewBox="0 0 24 24" aria-hidden="true"><path fill="#fff" d="M6.6 10.8a15.1 15.1 0 0 0 6.6 6.6l2.2-2.2a1 1 0 0 1 1-.25 11.4 11.4 0 0 0 3.6.57 1 1 0 0 1 1 1V20a1 1 0 0 1-1 1A17 17 0 0 1 3 4a1 1 0 0 1 1-1h3.5a1 1 0 0 1 1 1c0 1.25.2 2.45.57 3.57a1 1 0 0 1-.25 1z"/></svg>
          076 412 58 94
        </li>
        <li class="contact__item">
          <svg class="contact__icon" viewBox="0 0 24 24" aria-hidden="true"><path fill="#fff" d="M2 5h20v14H2z"/><path fill="none" stroke="#2f3032" stroke-width="1.8" d="M2.5 5.5 12 13l9.5-7.5"/></svg>
          sfellor@postkiv.ch
        </li>
        <li class="contact__item">
          <svg class="contact__icon" viewBox="0 0 24 24" aria-hidden="true"><g fill="none" stroke="#fff" stroke-width="2"><circle cx="12" cy="12" r="10"/><ellipse cx="12" cy="12" rx="4.5" ry="10"/><path d="M2 12h20M4 7h16M4 17h16"/></g></svg>
          www.fellor-di-vanti.ch
        </li>
      </ul>
    </div>
  </section>

  <section class="card card--back" aria-label="Rückseite">
    <div class="brand">
      <span class="brand__dot"></span>
      <span class="brand__name">Wege im Dialog</span>
    </div>
  </section>

</main>
</body>
</html>
```